Nine Rung Ledger Remedy Seminar

I would like a flyer to hand out to participants at the speeches that we give. We are a CPA firm that specializes in entrepreneurs and realtors. We would like a flyer that looks crisp and clean, that integrates our logo and our company colors (shades of blue & gold). We would like the wording to be as laid out in the attached documents, but design is up to you. We would like a picture to go along with each point and are open to ideas. The flyer should be one page, preferably just the front.

Colors
3176b5
fee18a

Requirements
Must have
• Our logo and the wording supplied.
• A picture to go along with each topic.
Nice to have
• Images that pop, clean look, professional.
Should not have
• Look messy.

```html
<!DOCTYPE html>
<html lang="en">
<head>
<meta charset="utf-8">
<title>Nine Rung Ledger Remedy Seminar Agenda</title>
<link href="https://fonts.googleapis.com/css2?family=Roboto+Condensed:ital,wght@0,400;0,700;1,400&family=Oswald:wght@500;600&family=Libre+Baskerville:ital,wght@1,700&display=swap" rel="stylesheet">
<style>
  :root {
    --brand-blue: #3176b5;
    --title-blue: #2a5ba8;
    --deep-blue: #1f3f8a;
    --brand-gold: #fee18a;
    --num-gold: #f7b51b;
    --num-orange: #f08a12;
    --ink: #2b2b2b;
    --sky-soft: #d6ebf8;
    --paper: #ffffff;
  }
  * { box-sizing: border-box; margin: 0; padding: 0; }
  html, body { width: 848px; height: 1200px; overflow: hidden; background: var(--paper); }
  .flyer {
    position: relative; width: 848px; height: 1200px; overflow: hidden;
    font-family: "Roboto Condensed", "Arial Narrow", sans-serif; color: var(--ink);
    background:
      radial-gradient(ellipse 520px 200px at 640px 20px, rgba(160,205,238,.75), rgba(214,235,248,0) 70%),
      radial-gradient(ellipse 700px 120px at 420px 150px, rgba(214,235,248,.6), rgba(255,255,255,0) 70%),
      radial-gradient(ellipse 900px 190px at 420px 1210px, rgba(254,214,90,.95), rgba(254,225,138,0) 70%),
      radial-gradient(ellipse 500px 140px at 120px 1120px, rgba(254,225,138,.7), rgba(255,255,255,0) 70%),
      var(--paper);
  }
  .brand { position: absolute; left: 43px; top: 46px; }
  .brand-name {
    display: flex; align-items: center; gap: 10px;
    font-family: "Oswald", sans-serif; font-weight: 600; font-size: 38px;
    line-height: 1; color: var(--deep-blue); letter-spacing: .5px;
  }
  .brand-mark { width: 14px; height: 14px; background: var(--num-gold); }
  .brand-tagline {
    margin-top: 22px; font-family: "Libre Baskerville", serif; font-style: italic;
    font-weight: 700; font-size: 10.5px; color: #222;
  }
  .agenda-title {
    position: absolute; left: 0; width: 848px; top: 190px; text-align: center;
    font-family: "Oswald", sans-serif; font-weight: 500; font-size: 25px;
    color: var(--title-blue); letter-spacing: .3px;
  }
  .title-rule {
    position: absolute; left: 190px; width: 470px; top: 241px; height: 2px;
    background: linear-gradient(90deg, rgba(200,200,200,0), #dcdcdc, rgba(200,200,200,0));
  }
  .art { position: absolute; border-radius: 10px; }
  .art-savings { left: 194px; top: 282px; width: 132px; height: 76px;
    background: radial-gradient(ellipse at 50% 60%, #c9a679, #a98255 70%, rgba(255,255,255,0) 72%); }
  .art-planning { left: 534px; top: 296px; width: 160px; height: 62px;
    background: linear-gradient(160deg, rgba(255,255,255,0), #e6e6e6 30%, #9ab3d8 55%, #e6e6e6 75%, rgba(255,255,255,0)); }
  .art-taxfree { left: 174px; top: 492px; width: 180px; height: 96px;
    background: radial-gradient(ellipse at 35% 60%, #b9955f, #8f6e45 55%, rgba(255,255,255,0) 70%),
                radial-gradient(circle at 78% 40%, #f2a81b, #e09a10 35%, rgba(255,255,255,0) 38%); }
  .art-child { left: 544px; top: 462px; width: 152px; height: 120px;
    background: radial-gradient(ellipse at 45% 55%, #7a6a5e, #c9bdb2 55%, rgba(255,255,255,0) 72%); }
  .art-receipt { left: 198px; top: 702px; width: 138px; height: 78px;
    background: radial-gradient(ellipse at 50% 50%, #f1f1f1, #d9d9d9 60%, rgba(255,255,255,0) 72%); }
  .art-fund { left: 558px; top: 684px; width: 108px; height: 96px;
    background: radial-gradient(ellipse at 50% 58%, #f3ead8, #dccfb2 60%, rgba(255,255,255,0) 72%); }
  .art-bulbs { left: 138px; top: 900px; width: 138px; height: 96px;
    background:
      radial-gradient(ellipse 30px 38px at 25% 38%, #9fb48f, #c8d3c0 70%, rgba(255,255,255,0) 72%),
      radial-gradient(ellipse 30px 38px at 78% 38%, #9fb48f, #c8d3c0 70%, rgba(255,255,255,0) 72%); }
  .step { position: absolute; }
  .step-num {
    position: absolute; left: 0; top: 0; width: 29px; height: 29px; border-radius: 50%;
    background: radial-gradient(circle at 40% 35%, var(--num-gold), var(--num-orange));
    color: #fff; font-family: "Oswald", sans-serif; font-weight: 600; font-size: 24px;
    line-height: 29px; text-align: center;
  }
  .step-text {
    position: absolute; top: 2px; left: 46px; font-size: 13px; line-height: 19.8px;
    text-align: justify;
  }
  .s1 { left: 70px; top: 377px; } .s1 .step-text { width: 286px; }
  .s2 { left: 70px; top: 592px; } .s2 .step-text { width: 286px; }
  .s3 { left: 70px; top: 792px; } .s3 .step-text { width: 286px; }
  .s4 { left: 442px; top: 377px; } .s4 .step-text { left: 38px; width: 278px; }
  .s5 { left: 442px; top: 586px; } .s5 .step-text { left: 38px; width: 278px; }
  .s6 { left: 442px; top: 786px; } .s6 .step-text { left: 38px; width: 278px; }
  .s7 { left: 70px; top: 902px; }
  .s7 .step-text { left: 230px; top: 8px; width: 456px; }
  .motto {
    position: absolute; left: 300px; top: 992px; width: 460px;
    font-family: "Oswald", sans-serif; font-weight: 600; font-size: 16px;
    color: var(--title-blue); letter-spacing: .2px;
  }
  .contact {
    position: absolute; right: 92px; top: 1064px; text-align: right;
    font-size: 14px; line-height: 20px; color: #333;
  }
  .contact .sep { margin: 0 8px; color: #777; }
  .contact .web { font-weight: 700; color: var(--deep-blue); }
</style>
</head>
<body>
<main class="flyer">
  <header class="brand">
    <div class="brand-name"><span>Clearwater Tally</span><span class="brand-mark"></span></div>
    <p class="brand-tagline">A Professional Accounting Corporation</p>
  </header>

  <h1 class="agenda-title">NINE RUNG LEDGER REMEDY SEMINAR AGENDA</h1>
  <div class="title-rule"></div>

  <div class="art art-savings" role="img" aria-label="Burlap money sacks labelled savings, stuffed with banknotes"></div>
  <div class="art art-planning" role="img" aria-label="Letter tiles spelling tax planning in a crossword"></div>
  <div class="art art-taxfree" role="img" aria-label="Money sack with coins beside an orange tax free road sign"></div>
  <div class="art art-child" role="img" aria-label="Young child in a hat and vest holding banknotes beside a piggy bank"></div>
  <div class="art art-receipt" role="img" aria-label="Curled paper receipt roll"></div>
  <div class="art art-fund" role="img" aria-label="Piggy bank labelled college fund with banknotes"></div>
  <div class="art art-bulbs" role="img" aria-label="Two light bulbs filled with rolled banknotes"></div>

  <section class="step s1"><span class="step-num">1</span>
    <p class="step-text">We will first show you how to eliminate much of your self-employment tax on your return by converting your business into an S Corporation. A business owner making over $120,000 per year can save about $12,000 per year by doing this.</p></section>
  <section class="step s2"><span class="step-num">2</span>
    <p class="step-text">We will show you how to get tax free income from your corporation by renting you home to the corporation for the board meetings. Many of our clients are getting up to $21,000 in tax free income which could put $8,400 cash into your pocket.</p></section>
  <section class="step s3"><span class="step-num">3</span>
    <p class="step-text">We will show you the easiest way to track your expenses so that the only thing you will have to do to have rock solid books is to take a picture of the receipt and throw it away. It doesn’t get any better than that.</p></section>
  <section class="step s4"><span class="step-num">4</span>
    <p class="step-text">Next, we show you the importance of tax planning and why it is critical to meet with your CPA before the end of the year and not just when you do your tax preparation.</p></section>
  <section class="step s5"><span class="step-num">5</span>
    <p class="step-text">We will show you how to hire your children and get $7,500 per child tax free. This will save you $3,000 per child in income tax reduction.</p></section>
  <section class="step s6"><span class="step-num">6</span>
    <p class="step-text">We will discuss how to make your child’s college education tax deductible. With college cost spiraling out of control this is a biggie. Most of our clients have a savings of about $12,000 per year of college.</p></section>
  <section class="step s7"><span class="step-num">7</span>
    <p class="step-text">Our grand finale is to show you how to use, not one, but two corporations to get a several hundred thousand dollar tax deferral, get an interest free loan from the government and use that money to grow your business and your wealth.</p></section>

  <p class="motto">IF THEY DRIVE BY WITH A MACHINE GUN YOU DON’T HAVE TO STAND UP.</p>

  <address class="contact" style="font-style:normal">
    Clearwater Tally, A Professional Accounting Corporation<br>
    2870 N. Oak Ave, Ste. B, Linden Vale, CA 95000<br>
    Phone: 555-014-2290 Fax: 555-014-2291<br>
    Dana@clearwatertallycpas.com<span class="sep">|</span>Reed@clearwatertallycpas.com<br>
    <span class="web">www.clearwatertallycpa.com</span>
  </address>
</main>
</body>
</html>
```